Kestrel Wiring - Electrician company flyers for new clients

I want a flyer that will be dropped into mailboxes and will hopefully stand out more that the ones i have tried to mock up. I have attached my latest design to give you an idea but it is rather boring.

The aim is obviously to entice new customers into calling me for any electrical work, mainly domestic but i also do commercial work.
I will also upload a photo of my business card so that it can be used as a reference and my website is www.kestrelwiring.co.nz for any extra information.

Ideally the flyer will be DL size
measurements from printmorrow is that's any help
Document Trim Size
99 x 210 mm
1169 x 2480 pixels
Full Bleed Size
102 x 213 mm
1205 x 2516 pixels

Target Market(s)

Domestic electrical works

Industry/Entity Type

Electrician

Requirements
Must have
• all of my contact details -
• Dean Forsyth
• Dean@kestrelwiring.co.nz
• 027 3815 942
• www.kestrelwiring.co.nz
• A little write up similar to the one written on my draft but there's probably alot of room for improvement as my writing skills are lacking.
Nice to have
• clear and concise writing so that people wont throw it away before reading

```html
<!DOCTYPE html>
<html lang="en">
<head>
<meta charset="utf-8">
<title>Kestrel Wiring – DL Flyer</title>
<link rel="stylesheet" href="https://fonts.googleapis.com/css2?family=Jost:wght@300;400&family=Open+Sans:wght@400;700&display=swap">
<style>
  :root {
    --backdrop: #7cdcf9;
    --paper: #ffffff;
    --ink-grey: #6b6b6b;
    --ink-body: #3a3a3a;
    --rule: #1a1a1a;
    --blue-light: #24a0dc;
    --blue-mid: #3b78c0;
    --blue-deep: #2067b4;
    --white: #ffffff;
  }
  html, body {
    margin: 0;
    padding: 0;
    width: 927px;
    height: 1200px;
    overflow: hidden;
    background: var(--backdrop);
  }
  .flyer {
    position: absolute;
    left: 186px;
    top: 20px;
    width: 556px;
    height: 1160px;
    background: var(--paper);
    overflow: hidden;
  }
  .flyer__shapes {
    position: absolute;
    inset: 0;
  }
  .brand {
    position: absolute;
    top: 66px;
    left: 0;
    width: 100%;
    display: flex;
    justify-content: center;
    align-items: center;
    gap: 12px;
    font-family: "Open Sans", sans-serif;
    font-weight: 700;
    font-size: 34px;
    letter-spacing: 1px;
    color: var(--ink-grey);
    text-transform: uppercase;
  }
  .brand__mark {
    width: 26px;
    height: 26px;
    background: var(--blue-light);
  }
  .headline {
    position: absolute;
    top: 174px;
    left: 0;
    width: 100%;
    margin: 0;
    text-align: center;
    font-family: "Open Sans", sans-serif;
    color: var(--ink-grey);
    font-weight: 400;
  }
  .headline__lead {
    display: block;
    font-size: 29px;
    letter-spacing: 1.6px;
    line-height: 40px;
  }
  .headline__trade {
    display: block;
    font-size: 33px;
    font-weight: 700;
    letter-spacing: 2.5px;
    line-height: 40px;
  }
  .rule {
    position: absolute;
    height: 2px;
    background: var(--rule);
  }
  .rule--long { top: 265px; left: 63px; width: 428px; }
  .rule--short { top: 670px; left: 153px; width: 248px; }
  .copy {
    position: absolute;
    left: 30px;
    width: 496px;
    margin: 0;
    text-align: center;
    font-family: "Jost", sans-serif;
    font-weight: 300;
    font-size: 22px;
    line-height: 32.3px;
    color: var(--ink-body);
  }
  .copy--intro { top: 300px; }
  .copy--local { top: 546px; }
  .photo-shadow {
    position: absolute;
    left: 76px;
    top: 694px;
    width: 413px;
    height: 209px;
    background: var(--blue-deep);
    opacity: 0.8;
  }
  .photo {
    position: absolute;
    left: 71px;
    top: 689px;
    width: 413px;
    height: 209px;
    background: linear-gradient(180deg, #d9d6d2 0%, #eeeeec 35%, #c9c8c6 60%, #e9e9e8 100%);
  }
  .contact {
    position: absolute;
    left: 23px;
    top: 944px;
    font-family: "Jost", sans-serif;
    font-weight: 300;
    color: var(--white);
  }
  .contact__cta {
    margin: 0;
    font-size: 25px;
    line-height: 34px;
    position: relative;
  }
  .contact__cta::after {
    content: "";
    position: absolute;
    left: 18px;
    top: 36px;
    width: 139px;
    height: 2px;
    background: var(--white);
  }
  .contact__details {
    margin: 20px 0 0;
    font-style: normal;
    font-size: 24px;
    line-height: 32.5px;
  }
  .contact__name { text-transform: uppercase; }
  .website {
    position: absolute;
    right: 26px;
    top: 1104px;
    font-family: "Jost", sans-serif;
    font-weight: 300;
    font-size: 23px;
    color: var(--white);
  }
</style>
</head>
<body>
  <main class="flyer">
    <svg class="flyer__shapes" viewBox="0 0 556 1160" width="556" height="1160" aria-hidden="true">
      <path fill="var(--blue-light)" d="M9 585 Q38 590 58 612 L220 780 L420 780 L546 658 L546 1151 L9 1151 Z"/>
      <path fill="var(--blue-mid)" d="M9 726 L209 920 L9 920 Z"/>
      <path fill="var(--blue-deep)" d="M209 1151 L546 840 L546 1151 Z"/>
    </svg>

    <div class="brand">
      <span class="brand__mark"></span>
      <span class="brand__name">Kestrel Wiring</span>
    </div>

    <h1 class="headline">
      <span class="headline__lead">Do you need a local and reliable</span>
      <span class="headline__trade">ELECTRICIAN</span>
    </h1>
    <div class="rule rule--long"></div>

    <p class="copy copy--intro">
      Specializing in residential and commerial<br>
      electrial services, we are dedicated to<br>
      providing customer service that is<br>
      second to none whether&nbsp; you need a small<br>
      wiring fix or the<br>
      full installation , we can get the job done<br>
      right.
    </p>

    <p class="copy copy--local">
      Based in Brownsbay ,we are your Local<br>
      Electricians<br>
      with our Main aim to keep&nbsp; our work
    </p>
    <div class="rule rule--short"></div>

    <div class="photo-shadow"></div>
    <div class="photo" role="img" aria-label="Photo of a switchboard with rows of circuit breakers"></div>

    <section class="contact">
      <p class="contact__cta">Contact us today!</p>
      <address class="contact__details">
        <span class="contact__name">Dean Forsyth</span><br>
        Dean@kestrelwiring.co.nz<br>
        027 3815 942
      </address>
    </section>

    <div class="website">www.kestrelwiring.co.nz</div>
  </main>
</body>
</html>
```